Business Card Design Project

Need a business card that stands my education platform as a whole but

Target Market(s)

Parents, families, expats in the middle east.

Industry/Entity Type

Education

Contact Information for Business Card

www.brightlane.ae
www.homesteadhub.ae
www.littlenestcarers.ae

+971552419736
helena@brightlane.ae

Font styles to use
Serif

Requirements
Must have
• Logo's and contact details

```html
<!DOCTYPE html>
<html lang="en">
<head>
<meta charset="utf-8">
<title>Brightlane Business Card</title>
<link rel="stylesheet" href="https://fonts.googleapis.com/css2?family=Crimson+Text:wght@400;600&display=swap">
<style>
  :root {
    --teal: #2f7390;
    --orange: #ee8748;
    --white: #ffffff;
    --backdrop: #a9a9a9;
    --card-w: 560px;
    --card-h: 320px;
  }
  * { margin: 0; padding: 0; box-sizing: border-box; }
  html, body {
    width: 1200px;
    height: 1011px;
    overflow: hidden;
    background: var(--backdrop);
  }
  .canvas {
    position: relative;
    width: 1200px;
    height: 1011px;
    display: flex;
    flex-direction: column;
    align-items: center;
    justify-content: center;
    gap: 60px;
    font-family: "Crimson Text", Georgia, serif;
  }
  .card {
    position: relative;
    width: var(--card-w);
    height: var(--card-h);
    overflow: hidden;
    box-shadow: 0 6px 18px rgba(0, 0, 0, 0.18);
  }

  /* Front */
  .card--front {
    background: var(--teal);
    display: flex;
    align-items: center;
    justify-content: center;
  }
  .brand {
    display: flex;
    align-items: center;
    gap: 14px;
    font-weight: 600;
  }
  .brand__dot {
    border-radius: 50%;
    flex: none;
  }
  .card--front .brand { color: var(--white); font-size: 44px; }
  .card--front .brand__dot { width: 30px; height: 30px; background: var(--white); }

  /* Back */
  .card--back {
    display: flex;
    background: var(--white);
  }
  .card__brand-panel {
    width: 36%;
    display: flex;
    align-items: center;
    justify-content: center;
  }
  .card--back .brand { color: var(--teal); font-size: 28px; gap: 9px; }
  .card--back .brand__dot { width: 18px; height: 18px; background: var(--teal); }
  .card__contact-panel {
    position: relative;
    flex: 1;
    background: var(--orange);
    display: flex;
    flex-direction: column;
    justify-content: center;
    padding-left: 34px;
  }
  .contact-list {
    list-style: none;
    color: var(--white);
    font-size: 19px;
    line-height: 1.3;
  }
  .card__accent-bar {
    position: absolute;
    right: 38px;
    bottom: 0;
    width: 96px;
    height: 12px;
    background: var(--teal);
  }
</style>
</head>
<body>
  <main class="canvas">
    <section class="card card--front" aria-label="Card front">
      <div class="brand">
        <span class="brand__dot"></span>
        <span class="brand__name">Brightlane</span>
      </div>
    </section>

    <section class="card card--back" aria-label="Card back">
      <div class="card__brand-panel">
        <div class="brand">
          <span class="brand__dot"></span>
          <span class="brand__name">Brightlane</span>
        </div>
      </div>
      <div class="card__contact-panel">
        <ul class="contact-list">
          <li>www.brightlane.ae</li>
          <li>www.homesteadhub.ae</li>
          <li>www.littlenestcarers.ae</li>
          <li>+971552419736</li>
          <li>helena@brightlane.ae</li>
        </ul>
        <span class="card__accent-bar"></span>
      </div>
    </section>
  </main>
</body>
</html>
```